QLV Fashion Design Company Needs a New Web Design, Please Click Me

Designers:

PLEASE NOTE: we only need the web page design, not a fully coded website.

Our brand's name is The Bright Quarry, our signature is print. our style is edgy and chic.

The old website is too messy. here's the address:
www.qlvstudio.com.cn

The new website's purpose is to show our brand/design and most importantly, sell products, So it should be a combination of a designer official website and online shopping. I want the whole style to be clean, edgy and pioneer, easy to understand. we need a sophisticated online shopping website.

The reference websites are:
merolatest.co.uk
www.pd-kor.com
lucasvemm.com
orbaduvi.com
talumerosapkin.com

Please beat their designs :)

Check out our lasted fashion show to get to know us more.

https://www.vidplexa.com/watch?v=ZkamWtrBnoLe&spfreload=10

The attachments are our Logo and some 2015 Look Book.
(Please let us know if you want to play with our print in this particular web design, we can send the source file.)
Updates

Designers, we really like the design of ameliadrovenko.com(we have attached a picture of the website) , Can we get a homepage like that? so the designs you submit will be 3 pages. The first one should be a page that only has Shop/Look. then the shop page, it should be nothing but our product which we will list the categories ourself. And the look page should contain all the info. such as news, about us and designers etc. Thank you all for your hard work, we really enjoyed the designs. Added Monday, November 03, 2014

Target Market(s)

Our target audiences are woman aged from 16-40 who like online shopping

Industry/Entity Type

Online Shopping

Number of Pages Required

3 page

Font styles to use
Serif
Sans Serif
Script

Requirements
Must have
• Designers,
• we really like the design of ameliadrovenko.com(we have attached a picture of the website) , Can we get a homepage like that? so the designs you submit will be 3 pages. The first one should be a page that only has Shop/Look. then the shop page, it should be nothing but our product which we will list the categories ourself. And the look page should contain all the info. such as news, about us and designers etc. Thank you all for your hard work, we really enjoyed the designs.

```html
<!DOCTYPE html>
<html lang="en">
<head>
<meta charset="utf-8">
<title>QLV Group — The Bright Quarry</title>
<link rel="stylesheet" href="https://fonts.googleapis.com/css2?family=Gelasio:wght@400;500&family=Roboto:wght@400;500&display=swap">
<style>
:root{
  --ink:#1e1e1e;
  --bar:#222222;
  --header:#363636;
  --red:#c0100f;
  --red-deep:#a20a0a;
  --rose:#e2343d;
  --hero-dark:#2c2c2c;
  --frame:#5a5a5a;
  --text:#3a3a3a;
  --muted:#777;
  --line:#e3e3e3;
  --white:#fff;
}
*{margin:0;padding:0;box-sizing:border-box}
html,body{width:1200px;height:1100px;overflow:hidden;background:var(--white)}
body{position:relative;font-family:"Roboto",Arial,sans-serif;color:var(--text)}
.abs{position:absolute}

/* top bar */
.topbar{left:0;top:0;width:1200px;height:30px;background:var(--bar)}
.social{left:225px;top:0;display:flex}
.social span{width:30px;height:30px;border-right:1px solid #3a3a3a;display:flex;align-items:center;justify-content:center}
.social span:first-child{border-left:1px solid #3a3a3a}
.social i{width:10px;height:10px;border-radius:50%;background:#eee;display:block}
.util{top:0;height:30px;display:flex;align-items:center;color:#eee;font-size:12px}
.search{left:750px;width:142px;border-left:1px solid #3a3a3a;padding-left:8px;gap:6px}
.login{left:892px;width:53px;border-left:1px solid #3a3a3a;justify-content:center}
.gear{left:945px;width:30px;background:#444;justify-content:center}

/* header */
.header{left:0;top:30px;width:1200px;height:60px;background:var(--header)}
.brand{left:227px;top:40px;display:flex;align-items:center;gap:8px;color:#fff}
.brand .dot{width:40px;height:40px;border-radius:50%;background:var(--red)}
.brand .name{font-family:"Gelasio",Georgia,serif;font-size:17px;letter-spacing:1.6px;line-height:18px;white-space:nowrap}
.headlinks{top:50px;left:798px;width:177px;display:flex;align-items:center;justify-content:space-between;color:#eee;font-size:11.5px;white-space:nowrap}

/* nav */
.nav{left:225px;top:90px;height:41px;display:flex}
.nav a{display:block;height:41px;padding:8px 0 0 12px;border-right:1px solid #ddd;text-decoration:none;color:#444;font-family:"Gelasio",Georgia,serif;white-space:nowrap;overflow:visible}
.nav a.active{background:#ececec}
.nav b{display:block;font-size:10.5px;font-weight:500;line-height:13px}
.nav small{display:block;font-size:8px;line-height:11px;color:#888}

/* hero */
.hero{left:0;top:131px;width:1200px;height:434px;background:var(--hero-dark);overflow:hidden}
.hero svg{position:absolute;left:0;top:0}
.thumb{left:225px;width:184px;height:118px;border:8px solid var(--frame);background:#555}
.thumb.add{top:161px;background:var(--red);display:flex;align-items:center;justify-content:center}
.thumb.p1{top:286px;background:linear-gradient(90deg,#7e8284,#c9ccce 60%,#8a8d90)}
.thumb.p2{top:411px;background:linear-gradient(90deg,#e9e7e3,#f4f3f1)}
.shop{left:326px;top:366px;background:#222;color:#fff;font-size:10px;padding:5px 8px;white-space:nowrap}
.slider{left:416px;top:161px;width:559px;height:368px;border:8px solid #7a4040;background:linear-gradient(90deg,#1d2d4a 0%,#3b5d94 35%,#5c86c4 58%,#8fb6e6 80%,#3c63a2 100%)}
.arrow{top:329px;width:36px;height:36px;background:#111;display:flex;align-items:center;justify-content:center}
.slide-kicker{left:416px;width:559px;top:384px;text-align:center;color:#fff;font-size:10px;letter-spacing:3.6px;white-space:nowrap}
.slide-title{left:416px;width:559px;top:398px;text-align:center;color:#fff;font-size:35px;line-height:42px;font-family:"Gelasio",Georgia,serif;white-space:nowrap}
.slide-brand{left:416px;width:559px;top:451px;text-align:center;color:#fff;font-size:12px;font-weight:500;white-space:nowrap}
.slide-col{left:416px;width:559px;top:468px;text-align:center;color:#fff;font-size:10px;letter-spacing:4px}

/* statement */
.statement{left:0;width:1200px;top:594px;text-align:center;font-family:"Gelasio",Georgia,serif;font-size:18.5px;color:#444;line-height:27px}
.statement em{font-style:normal;color:var(--rose)}

.section-title{left:227px;top:669px;font-family:"Gelasio",Georgia,serif;font-size:13px;color:#333}
.hatch{left:389px;top:673px;width:586px;height:9px;background:repeating-linear-gradient(135deg,#d5d5d5 0 1px,transparent 1px 4px)}

/* cards */
.card{top:707px;width:177px;height:307px;border:1px solid var(--line);background:#fff}
.card .photo{position:absolute;left:12px;top:13px;width:150px;height:170px;background:linear-gradient(135deg,#7dc7e4,#b7e3f2 50%,#59b3d8)}
.card h3{position:absolute;top:201px;left:0;width:100%;text-align:center;font-family:"Gelasio",Georgia,serif;font-weight:400;font-size:10.5px;color:#333;white-space:nowrap}
.card p{position:absolute;top:224px;left:0;width:100%;text-align:center;font-size:9.5px;line-height:15px;color:#444;white-space:nowrap}
.card p.left{text-align:left;left:13px;width:auto}
.card hr{position:absolute;top:265px;left:0;width:100%;border:0;border-top:1px solid var(--line)}
.card .btn{position:absolute;left:10px;top:272px;width:156px;height:28px;background:var(--red);color:#fff;font-size:11px;letter-spacing:2.5px;display:flex;align-items:center;justify-content:center}
.card .btn.dark{background:#3b3b3b}

/* footer teaser */
.band{left:0;top:1055px;width:1200px;height:45px;background:var(--red-deep)}
.tile{top:1087px;height:13px;width:188px}
</style>
</head>
<body>

<div class="abs topbar"></div>
<div class="abs social" aria-label="Social links">
  <span><i></i></span><span><i></i></span><span><i></i></span><span><i></i></span><span><i></i></span>
</div>
<div class="abs util search">
  <svg width="18" height="18" viewBox="0 0 18 18"><circle cx="7.5" cy="7.5" r="6" fill="none" stroke="#eee" stroke-width="1.6"/><line x1="12" y1="12" x2="17" y2="17" stroke="#eee" stroke-width="1.8"/></svg>
  Search
</div>
<div class="abs util login">Login</div>
<div class="abs util gear">
  <svg width="18" height="18" viewBox="0 0 18 18"><circle cx="9" cy="9" r="6.5" fill="none" stroke="#eee" stroke-width="1.5" stroke-dasharray="3 1.6"/><circle cx="9" cy="9" r="2.5" fill="none" stroke="#eee" stroke-width="1.4"/></svg>
</div>

<div class="abs header"></div>
<div class="abs brand">
  <span class="dot"></span>
  <span class="name">QLV GROUP<br>THE BRIGHT QUARRY</span>
</div>
<div class="abs headlinks">
  <svg width="18" height="16" viewBox="0 0 18 16"><rect x="1" y="1" width="16" height="10" fill="none" stroke="#eee" stroke-width="1.4"/><line x1="6" y1="15" x2="12" y2="15" stroke="#eee" stroke-width="1.4"/><line x1="9" y1="11" x2="9" y2="15" stroke="#eee" stroke-width="1.4"/></svg>
  <span>Product tour</span>
  <svg width="18" height="16" viewBox="0 0 18 16"><rect x="1" y="5" width="16" height="10" fill="none" stroke="#eee" stroke-width="1.4"/><path d="M4 5V1h10v4M4 9h10M4 12h10" fill="none" stroke="#eee" stroke-width="1.2"/></svg>
  <span>Get it now</span>
</div>

<nav class="abs nav">
  <a class="active" style="width:90px"><b>HOME</b><small>QLV GROUP</small></a>
  <a style="width:99px"><b>ABOUT US</b><small>QLV GROUP</small></a>
  <a style="width:99px"><b>SERVICES</b><small>QLV GROUP</small></a>
  <a style="width:75px"><b>PRODUCTS</b><small>QLV GROUP</small></a>
  <a style="width:108px;padding-left:11px"><b>NEWS &amp; EVENTS</b><small>QLV GROUP</small></a>
  <a style="border-right:0"><b>CONTACT US</b><small>QLV GROUP</small></a>
</nav>

<section class="abs hero">
  <svg width="1200" height="434"><polygon points="760,0 1200,0 1200,434 455,434" fill="var(--red)"/></svg>
</section>
<div class="abs thumb add">
  <svg width="32" height="32"><line x1="16" y1="1" x2="16" y2="31" stroke="#fff" stroke-width="2"/><line x1="1" y1="16" x2="31" y2="16" stroke="#fff" stroke-width="2"/></svg>
</div>
<div class="abs thumb p1" role="img" aria-label="Model in a white shirt and black skirt"></div>
<div class="abs shop">SHOP NOW !</div>
<div class="abs thumb p2" role="img" aria-label="Model in a straw hat and white top"></div>

<div class="abs slider" role="img" aria-label="Model in a blue printed shirt against a blue textured backdrop"></div>
<div class="abs arrow" style="left:432px"><svg width="12" height="16"><polyline points="9,2 3,8 9,14" fill="none" stroke="#ddd" stroke-width="2"/></svg></div>
<div class="abs arrow" style="left:925px"><svg width="12" height="16"><polyline points="3,2 9,8 3,14" fill="none" stroke="var(--rose)" stroke-width="2.4"/></svg></div>
<div class="abs slide-kicker">LOREM IPSUM IS SIMPLY DUMMY TEXT</div>
<div class="abs slide-title">LOREM ISPUM DUMMY</div>
<div class="abs slide-brand">THE BRIGHT QUARRY</div>
<div class="abs slide-col">COLLECTION</div>

<div class="abs statement">WE MAKE INSPIRATIONAL DESIGNS COME ALIVE THROUGH<br><em>INNOVATION</em> AND <em>PERFECTIONISM</em></div>

<div class="abs section-title">FEATURED BRAND</div>
<div class="abs hatch"></div>

<article class="abs card" style="left:225px">
  <div class="photo" role="img" aria-label="Model in a blue printed jumpsuit"></div>
  <h3>LOREM IPSUM DUMMY</h3>
  <p class="left">Lorem Ipsum is simply dummy text<br>of the printing.</p>
  <hr><div class="btn dark">VIEW MORE</div>
</article>
<article class="abs card" style="left:416px">
  <div class="photo" role="img" aria-label="Model in a blue printed dress"></div>
  <h3>LOREM IPSUM DUMMY</h3>
  <p>Lorem Ipsum is simply dummy text<br>of the printing.</p>
  <hr><div class="btn">VIEW MORE</div>
</article>
<article class="abs card" style="left:608px">
  <div class="photo" role="img" aria-label="Model in a printed crop top and white trousers"></div>
  <h3>LOREM IPSUM DUMMY</h3>
  <p>Lorem Ipsum is simply dummy text<br>of the printing.</p>
  <hr><div class="btn">VIEW MORE</div>
</article>
<article class="abs card" style="left:799px">
  <div class="photo" role="img" aria-label="Model in a blue printed top and shorts"></div>
  <h3>LOREM IPSUM DUMMY</h3>
  <p>Lorem Ipsum is simply dummy text<br>of the printing.</p>
  <hr><div class="btn">VIEW MORE</div>
</article>

<div class="abs band"></div>
<div class="abs tile" style="left:225px;background:#3a3a3a" role="img" aria-label="Dark lookbook photo"></div>
<div class="abs tile" style="left:413px;background:#fff"></div>
<div class="abs tile" style="left:600px;background:#ece6de" role="img" aria-label="Light lookbook photo"></div>
<div class="abs tile" style="left:788px;width:187px;background:#fff"></div>

</body>
</html>
```